Kickbut Home Page Design built to Sell

We need a new home page layout. The website is working now but we need a refresh. Our business has slowed down since a few years ago. We need to show we build ecommerce and membership websites. Here is the page now: https://www.qelvartinbuild.graphics/new-home/

Target Market(s)

Women, solopreneurs, artists, politicians

Industry/Entity Type

Design Agency

Number of Pages Required

1 page

Font styles to use
Sans Serif

Colors
b8a6cd
fabb94
acd136
00a990

Requirements
Must have
• Video header
Section for text and Step process similar to this website: https://tovarellaplexworks.com/ [This is out sister company]
Places for images.
Call to action lead gen form and Get a quote.
The menu should show WEB, PRINT, VIDEO
Nice to have
• I LOVE this company: https://plumeravik.com/guide/
Area for testimonials
Should not have
• We don't want a duplicate of https://tovarellaplexworks.com/

```html
<!DOCTYPE html>
<html lang="en">
<head>
<meta charset="utf-8">
<title>Qelvartin – Web Design Agency</title>
<link href="https://fonts.googleapis.com/css2?family=Oswald:wght@400;500&family=Lato:ital,wght@0,400;0,700;1,400&display=swap" rel="stylesheet">
<style>
:root{
  --teal:#00a990;
  --teal-dark:#0b8f73;
  --lime:#acd136;
  --ink:#111;
  --text:#333;
  --muted:#555;
  --paper:#fff;
  --mist:#f1f1f1;
  --footer:#050505;
}
*{box-sizing:border-box;margin:0;padding:0}
html,body{width:1200px;height:5128px;overflow:hidden}
body{position:relative;font-family:'Lato',sans-serif;color:var(--text);background:var(--paper)}
.abs{position:absolute}
.head{font-family:'Oswald',sans-serif;font-weight:500;color:var(--ink);text-transform:uppercase}
.photo{position:absolute}

/* hero */
.hero{position:absolute;left:0;top:0;width:1200px;height:610px;background:linear-gradient(110deg,#3d3a37 0%,#6e665e 45%,#8b8580 70%,#5a5550 100%)}
.hero-shade{position:absolute;inset:0;background:linear-gradient(90deg,rgba(0,0,0,.45),rgba(0,0,0,.05))}
.brand{left:110px;top:18px;color:#fff;font-family:'Oswald',sans-serif;font-size:38px;font-weight:500;letter-spacing:1px}
.brand small{display:block;font-family:'Lato',sans-serif;font-size:9px;letter-spacing:2px;margin-top:-4px}
.nav{top:34px;left:566px;display:flex;gap:30px;color:#fff;font-family:'Oswald',sans-serif;font-size:17px}
.btn{display:flex;align-items:center;justify-content:center;border-radius:26px;font-family:'Oswald',sans-serif;text-transform:uppercase;font-size:16px}
.btn-solid{background:var(--teal);color:#fff}
.btn-line{border:2px solid #fff;color:#fff;font-family:'Lato',sans-serif;font-size:13px;font-weight:700}
.hero-title{left:114px;top:252px;color:#fff;font-family:'Oswald',sans-serif;font-size:32px;line-height:42px;text-transform:uppercase}
.play{left:666px;top:270px}

/* services */
.section-title{width:1200px;text-align:center;font-size:38px}
.card{position:absolute;top:750px;width:236px;height:352px;background:#fff;box-shadow:0 2px 6px rgba(0,0,0,.12)}
.card .photo{left:0;top:0;width:236px;height:164px}
.card h3{position:absolute;top:184px;width:100%;text-align:center;font-size:18px}
.card p{position:absolute;top:220px;left:14px;right:14px;text-align:center;font-size:13px;line-height:22px}

/* agency band */
.band{position:absolute;left:0;top:1188px;width:1200px;height:557px;background:linear-gradient(100deg,var(--teal-dark),var(--teal) 55%,#1fb895)}
.band h2{left:110px;top:1300px;color:#fff;font-size:34px}
.band-lead{left:110px;top:1360px;width:430px;color:#fff;font-size:14px;line-height:23px}
.band-body{left:110px;top:1438px;width:440px;color:#fff;font-size:12px;line-height:23px}

/* process */
.step{position:absolute;left:645px;width:450px}
.step .icon{position:absolute;left:0;top:0;width:84px;height:84px;border-radius:50%;background:var(--lime)}
.step h4{position:absolute;left:100px;top:6px;font-size:20px;white-space:nowrap}
.step p{position:absolute;left:100px;top:40px;width:340px;font-size:15px;line-height:20px;color:#222}

/* testimonials */
.quote{position:absolute;top:2570px;width:440px;text-align:center}
.quote .avatar{width:120px;height:120px;border-radius:50%;margin:0 auto;background:linear-gradient(#cfd3d6,#8e969b)}
.quote blockquote{margin-top:22px;font-style:italic;font-size:14px;line-height:27.5px;color:#444}
.quote .name{margin-top:20px;font-size:16px;color:#222}
.quote .stars{color:#f2b705;font-size:17px;letter-spacing:1px}
.quote .role{margin-top:6px;font-size:14px;color:#555}

/* work grid */
.tile{position:absolute;width:400px;display:flex;align-items:center;justify-content:center;text-align:center;color:#fff;font-family:'Oswald',sans-serif;font-size:24px;line-height:34px;text-transform:uppercase}
.tile.teal{background:var(--teal)}
.tile.lime{background:var(--lime)}

/* form */
.quote-area{position:absolute;left:0;top:4068px;width:1200px;height:657px;background:var(--mist)}
.quote-card{position:absolute;left:246px;top:4150px;width:708px;height:520px;background:#fff;box-shadow:0 2px 8px rgba(0,0,0,.08)}
.field{position:absolute;height:48px;border:1px solid #cfcfcf;font-size:13px;color:#555;padding:14px 18px}

/* footer */
.footer{position:absolute;left:0;top:4725px;width:1200px;height:403px;background:var(--footer);color:#fff}
.fcol{position:absolute;top:4790px}
.fcol h5{font-family:'Oswald',sans-serif;font-weight:500;font-size:17px;text-transform:uppercase;margin-bottom:14px}
.fcol li{list-style:none;font-size:14px;line-height:19px;margin-bottom:14px}
.rule{left:110px;top:5065px;width:980px;height:1px;background:#333}
.copy{top:5092px;width:1200px;text-align:center;font-size:13px;color:#fff}
</style>
</head>
<body>

<!-- Hero -->
<section class="hero" role="img" aria-label="Video header: two women working at laptops in a bright office"><div class="hero-shade"></div></section>
<div class="abs brand">QELVARTIN<small>GRAPHICS WEB VIDEO CONSULTANTS</small></div>
<nav class="abs nav"><span>WEB</span><span>PRINT</span><span>VIDEO</span><span>CONTACT</span></nav>
<div class="abs btn btn-solid" style="left:898px;top:20px;width:188px;height:48px">Get a Quote</div>
<h1 class="abs hero-title">Lead generating websites that<br>move your business forward</h1>
<div class="abs btn btn-line" style="left:116px;top:368px;width:172px;height:46px">VIEW OUR WORK</div>
<svg class="abs play" width="80" height="80" viewBox="0 0 80 80"><circle cx="40" cy="40" r="38" fill="rgba(255,255,255,.85)"/><circle cx="40" cy="40" r="24" fill="var(--teal)"/><path d="M34 29 L52 40 L34 51Z" fill="#fff"/></svg>

<!-- What we do -->
<h2 class="abs head section-title" style="top:682px">What we do</h2>
<article class="card" style="left:111px"><div class="photo" role="img" aria-label="Laptop with gear icon on a desk" style="background:linear-gradient(#2d2d2d,#6d6a66)"></div><h3 class="head">Website Maintenance</h3><p>Want to keep your business growing? Your website is crucial to your growth and success. When operating seamlessly with your goals.</p></article>
<article class="card" style="left:359px"><div class="photo" role="img" aria-label="Workshop screen showing a landscape" style="background:linear-gradient(#3b5c6b,#8aa2a8)"></div><h3 class="head">Workshops</h3><p>We offer workshops to business, schools, non-profits, and organizations. We can tailor the workshop to your organizations if needed.</p></article>
<article class="card" style="left:607px"><div class="photo" role="img" aria-label="Artist working at monitors" style="background:linear-gradient(#9aa0a6,#d6d6d2)"></div><h3 class="head">Artist Website</h3><p>When you are in the art world you need to show your craft to get exposure, gigs and sales. We love working with artists that value good design!</p></article>
<article class="card" style="left:855px"><div class="photo" role="img" aria-label="Hand sketching logo concepts" style="background:linear-gradient(#e4e6ea,#b8bcc4)"></div><h3 class="head">Logo Design</h3><p>Want to keep your business growing? Your website is crucial to your growth and success. When operating seamlessly with your goals.</p></article>

<!-- Agency band -->
<section class="band"></section>
<h2 class="abs head" style="left:110px;top:1300px;color:#fff;font-size:34px">We are a web design agency</h2>
<p class="abs band-lead">We help brands sell online with beautifully designed websites and effective digital marketing strategies that deliver results &amp; help your business grow.</p>
<p class="abs band-body">Tovarella Plexworks is a New England web design agency providing high quality, professional and reliable website - webpage design and graphic design services to individuals, nonprofits, small - medium sized businesses, and political campaigns. We are a small team of highly professional web consultants with over 20 years of knowledge and experience and we'd love to help you too!</p>
<div class="abs btn btn-line" style="left:110px;top:1596px;width:190px;height:48px;font-family:'Oswald',sans-serif;font-size:16px;font-weight:400">CONTACT US</div>
<svg class="abs" style="left:885px;top:1450px" width="240" height="270"><defs><pattern id="dots" width="16" height="16" patternUnits="userSpaceOnUse"><circle cx="3" cy="3" r="2" fill="#fff"/></pattern></defs><rect x="0" y="190" width="240" height="80" fill="url(#dots)"/><rect x="200" y="0" width="40" height="270" fill="url(#dots)"/></svg>
<div class="photo" role="img" aria-label="Smiling designer in glasses beside a desktop design workspace" style="left:612px;top:1285px;width:476px;height:380px;background:linear-gradient(110deg,#d9c8b6,#f3f1ee 55%,#c7ccd2)"></div>

<!-- Process -->
<div class="photo" role="img" aria-label="Woman working at a computer in an office" style="left:0;top:1745px;width:600px;height:630px;background:linear-gradient(135deg,#7e7c79,#c9c6c1 60%,#8f8b86)"></div>
<h2 class="abs head" style="left:645px;top:1816px;font-size:38px">The process is simple</h2>
<div class="step" style="top:1895px"><svg class="icon" viewBox="0 0 84 84"><circle cx="42" cy="42" r="42" fill="var(--lime)"/><path d="M30 52h24M34 52V38h16v14M38 32h8" stroke="#fff" stroke-width="3" fill="none"/></svg><h4 class="head">Step 1 - Tell us your needs</h4><p>Fill out our easy questionnaire so we can understand your problems.</p></div>
<div class="step" style="top:2010px"><svg class="icon" viewBox="0 0 84 84"><circle cx="42" cy="42" r="42" fill="var(--lime)"/><path d="M30 28c0 16 10 26 26 26l3-7-7-4-4 4c-5-2-9-6-11-11l4-4-4-7z" fill="#fff"/></svg><h4 class="head">Step 2 - Phone call</h4><p>Book a time to have a chat in case we have more question about your goals.</p></div>
<div class="step" style="top:2125px"><svg class="icon" viewBox="0 0 84 84"><circle cx="42" cy="42" r="42" fill="var(--lime)"/><rect x="28" y="24" width="28" height="36" fill="none" stroke="#fff" stroke-width="3"/><path d="M33 34h18M33 42h18M33 50h10" stroke="#fff" stroke-width="3"/></svg><h4 class="head">Step 3 - Custom quote arrives</h4><p>Once we have made your plan, we'll get to work to build and launch your new website.</p></div>
<div class="abs btn btn-solid" style="left:652px;top:2240px;width:188px;height:50px">Get a Quote</div>

<!-- Testimonials -->
<h2 class="abs head section-title" style="top:2452px">Why our clients love us</h2>
<p class="abs" style="top:2512px;width:1200px;text-align:center;font-size:16px">AND WHY THEY KEEP COMING BACK.</p>
<svg class="abs" style="left:92px;top:2786px" width="16" height="30"><path d="M14 2 L2 15 L14 28" stroke="#222" stroke-width="2" fill="none"/></svg>
<svg class="abs" style="left:1092px;top:2786px" width="16" height="30"><path d="M2 2 L14 15 L2 28" stroke="#222" stroke-width="2" fill="none"/></svg>
<div class="quote" style="left:135px"><div class="avatar" role="img" aria-label="Client portrait"></div><blockquote>Rowan Ellery was great to work with and extremely knowledgeable and accessible. I especially appreciated his well thought out design process and the client videos he created to walk me through various stages of it. I received lots of great feedback on the visual look, user-friendliness, and rich content of my website throughout the campaign and was re-elected overwhelmingly. I highly recommend Rowan and Tovarella Designs for your next project!</blockquote><div class="name">MARTIN OSGOOD</div><div class="stars">★★★★★</div><div class="role">MAYOR, BROOKFIELD, MA</div></div>
<div class="quote" style="left:623px"><div class="avatar" role="img" aria-label="Client portrait"></div><blockquote>Rowan Ellery was great to work with and extremely knowledgeable and accessible. I especially appreciated his well thought out design process and the client videos he created to walk me through various stages of it. I received lots of great feedback on the visual look, user-friendliness, and rich content of my website throughout the campaign and was re-elected overwhelmingly. I highly recommend Rowan and Tovarella Designs for your next project!</blockquote><div class="name">MARTIN OSGOOD</div><div class="stars">★★★★★</div><div class="role">MAYOR, BROOKFIELD, MA</div></div>
<svg class="abs" style="left:553px;top:3062px" width="96" height="16"><circle cx="8" cy="8" r="7" fill="#111"/><circle cx="34" cy="8" r="7" fill="#aaa"/><circle cx="60" cy="8" r="7" fill="#aaa"/><circle cx="86" cy="8" r="7" fill="#aaa"/></svg>

<!-- Work -->
<h2 class="abs head section-title" style="top:3150px">Examples of our work</h2>
<div class="photo" role="img" aria-label="Laptop showing a website" style="left:0;top:3240px;width:400px;height:262px;background:linear-gradient(135deg,#dadada,#6a6a6a)"></div>
<div class="tile lime" style="left:0;top:3502px;height:150px">The standard lorem ipsum<br>passage, used since</div>
<div class="photo" role="img" aria-label="Monitor with a design project" style="left:0;top:3652px;width:400px;height:263px;background:linear-gradient(135deg,#1e1e1e,#77808a)"></div>
<div class="tile teal" style="left:0;top:3915px;height:153px">The standard lorem ipsum<br>passage, used since</div>
<div class="tile teal" style="left:400px;top:3240px;height:152px">The standard lorem ipsum<br>passage, used since</div>
<div class="photo" role="img" aria-label="Hands using a tablet" style="left:400px;top:3392px;width:400px;height:260px;background:linear-gradient(135deg,#c9c9c9,#5e5e5e)"></div>
<div class="tile lime" style="left:400px;top:3652px;height:153px">The standard lorem ipsum<br>passage, used since</div>
<div class="photo" role="img" aria-label="Laptop on a bright desk" style="left:400px;top:3805px;width:400px;height:263px;background:linear-gradient(135deg,#f0efed,#a7a6a3)"></div>
<div class="photo" role="img" aria-label="Laptop showing a 3D model" style="left:800px;top:3240px;width:400px;height:262px;background:linear-gradient(135deg,#7a7a7a,#1f1f1f)"></div>
<div class="tile lime" style="left:800px;top:3502px;height:150px">The standard lorem ipsum<br>passage, used since</div>
<div class="photo" role="img" aria-label="Designer at a dual monitor setup" style="left:800px;top:3652px;width:400px;height:263px;background:linear-gradient(135deg,#2a2a2a,#8a7d72)"></div>
<div class="tile teal" style="left:800px;top:3915px;height:153px">The standard lorem ipsum<br>passage, used since</div>

<!-- Quote form -->
<section class="quote-area"></section>
<form class="quote-card" aria-label="Get a quote"></form>
<h2 class="abs head section-title" style="top:4196px">Get a quote</h2>
<div class="field" style="left:304px;top:4268px;width:292px">First Name</div>
<div class="field" style="left:604px;top:4268px;width:292px">Last Name</div>
<div class="field" style="left:304px;top:4325px;width:292px">Email Address</div>
<div class="field" style="left:604px;top:4325px;width:292px">Phone</div>
<div class="field" style="left:304px;top:4383px;width:292px">Company Name</div>
<div class="field" style="left:604px;top:4383px;width:292px">Location</div>
<div class="field" style="left:304px;top:4443px;width:592px;height:100px">Meesage</div>
<div class="abs btn btn-solid" style="left:506px;top:4560px;width:188px;height:50px">Submit</div>

<!-- Footer -->
<footer class="footer"></footer>
<div class="fcol" style="left:110px"><h5>More</h5><ul><li>Blog</li><li>Praise</li><li>Internships</li><li>Website Audits</li><li>Local Listing<br>Resource</li></ul></div>
<div class="fcol" style="left:356px"><h5>Pages</h5><ul><li>Who We Are</li><li>Our Clients</li><li>Our Process</li><li>Our Work</li><li>Contact</li><li>Services</li></ul></div>
<div class="fcol" style="left:551px"><h5>Additional Resources</h5><ul><li>FAQ</li><li>Privacy policy</li><li>Terms and conditions</li></ul></div>
<div class="fcol" style="left:843px"><h5>Get in touch!</h5><ul>
<li><svg width="10" height="14" viewBox="0 0 10 14"><path d="M5 0a5 5 0 0 0-5 5c0 4 5 9 5 9s5-5 5-9a5 5 0 0 0-5-5z" fill="#fff"/></svg> 18 Linden Row, Westbrook<br>&nbsp;&nbsp;&nbsp;MA 01077</li>
<li><svg width="12" height="12" viewBox="0 0 12 12"><path d="M1 1c0 6 4 10 10 10l1-3-3-2-2 2C5 7 4 6 3 4l2-2-2-3z" fill="#fff"/></svg> 1-555-014-2290</li>
<li><svg width="13" height="10" viewBox="0 0 13 10"><rect width="13" height="10" fill="#fff"/><path d="M0 0l6.5 5L13 0" stroke="#000" fill="none"/></svg> rowan@tovarellaplexworks.com</li></ul></div>
<div class="abs rule"></div>
<p class="abs copy">© 2021 Tovarella Development. All Rights Reserved. Westbrook MA 01077</p>

</body>
</html>
```